Fitness Equipment Repair Business Needs a Catchy New Business Card

We have an existing business card, however, it is quite plain and boring. We are expanding primarily in the commercial area (gyms, studios, apartment complexes etc). The business card will serve as eye candy to those managers/owners that can't be met for a face to face.
Originally I was planning for a brochure as well, but all of our information is better summarized on our website. (brookmotionservice.ca).
I would like the card to match the colour scheme of the website and utilize the logo. It should have a professional clean feel to it, however, a little colouring outside the lines wouldn't hurt.
The example card is for my service technician (Colin Harstad). If possible I would like to be able to edit the text to use for more than one person.

Industry/Entity Type

Appliance Repair

Contact Information for Business Card

Clean, crisp and professional but needs to be eye catching. Preferably using the black, white and red colour scheme matching the website. Double sided would be nice, but is not necessary.

Colors
ec1f27
ffffff
000000

Requirements
Must have
• Must be able to edit name, phone number and title to use for multiple people. Must show the company website (brookmotionservice.ca).

```html
<!DOCTYPE html>
<html lang="en">
<head>
<meta charset="utf-8">
<title>Brook Motion Service – Business Card</title>
<link href="https://fonts.googleapis.com/css2?family=Marcellus+SC&display=swap" rel="stylesheet">
<style>
  :root {
    --canvas-grey: #808080;
    --card-black: #000000;
    --card-charcoal: #2a2a2a;
    --brand-red: #ec1f27;
    --brand-red-deep: #a3161c;
    --text-white: #ffffff;
    --art-grey: #3a3a3a;
  }
  html, body {
    margin: 0;
    padding: 0;
    width: 1200px;
    height: 1000px;
    overflow: hidden;
    background: var(--canvas-grey);
  }
  .business-card {
    position: absolute;
    left: 336px;
    top: 350px;
    width: 526px;
    height: 301px;
    font-family: "Marcellus SC", serif;
    color: var(--text-white);
    overflow: hidden;
  }
  .business-card .card-text {
    -webkit-text-stroke: 0.35px var(--text-white);
    white-space: nowrap;
  }
  .card-top {
    position: absolute;
    inset: 0 0 87px 0;
    background: radial-gradient(ellipse at 60% 35%, var(--card-charcoal) 0%, #111 45%, var(--card-black) 80%);
  }
  .technician-art {
    position: absolute;
    left: 18px;
    top: 14px;
    width: 132px;
    height: 190px;
    border-radius: 6px;
    background: linear-gradient(160deg, var(--art-grey), #151515);
  }
  .brand-name {
    position: absolute;
    left: 26px;
    top: 168px;
    margin: 0;
    font-size: 32px;
    line-height: 1;
    letter-spacing: 1px;
    color: var(--text-white);
  }
  .company-title {
    position: absolute;
    left: 132px;
    top: 11px;
    margin: 0;
    font-size: 29px;
    line-height: 1;
    letter-spacing: 0.4px;
    font-weight: 400;
  }
  .tagline {
    position: absolute;
    left: 133px;
    top: 39px;
    margin: 0;
    font-size: 10px;
    line-height: 12px;
    letter-spacing: 0.2px;
  }
  .name-band {
    position: absolute;
    left: 134px;
    top: 110px;
    right: 0;
    height: 52px;
    background: linear-gradient(90deg, rgba(0,0,0,0) 0%, var(--card-black) 12%, var(--card-black) 88%, rgba(0,0,0,0.6) 100%);
  }
  .person-name {
    position: absolute;
    left: 167px;
    top: 117px;
    margin: 0;
    font-size: 25px;
    line-height: 1;
    font-weight: 400;
  }
  .person-role {
    position: absolute;
    left: 191px;
    top: 140px;
    margin: 0;
    font-size: 13.5px;
    line-height: 14px;
    letter-spacing: 0.2px;
  }
  .card-bottom {
    position: absolute;
    left: 0;
    right: 0;
    bottom: 0;
    height: 87px;
    background: linear-gradient(180deg, var(--brand-red) 0%, var(--brand-red-deep) 100%);
  }
  .contact-block {
    position: absolute;
    left: 264px;
    top: 4px;
    margin: 0;
    font-style: normal;
    font-size: 11px;
    line-height: 11px;
  }
  .contact-block p { margin: 0; }
  .contact-block .address { margin-bottom: 11px; }
  .contact-block .lines p { line-height: 11.5px; }
</style>
</head>
<body>
  <section class="business-card">
    <div class="card-top">
      <div class="technician-art" role="img" aria-label="Line illustration of a muscular technician in a hard hat holding a wrench"></div>
      <p class="brand-name">BMS</p>
      <h1 class="company-title card-text">BROOK MOTION SERVICE</h1>
      <p class="tagline card-text">WHEN YOUR EQUIPMENT CAN'T FINISH THE WORKOUT, GIVE US A CALL!</p>
      <div class="name-band"></div>
      <h2 class="person-name card-text">COLIN HARSTAD</h2>
      <p class="person-role card-text">SERVICE TECHNICIAN</p>
    </div>
    <div class="card-bottom">
      <address class="contact-block card-text">
        <div class="address">
          <p>1875 LARCHMONT ROAD NW</p>
          <p>GREYFIELD AB T4K 2P8</p>
        </div>
        <div class="lines">
          <p>PERSONAL: 555-314-2087</p>
          <p>SERVICE LINE: 555-640-9132</p>
          <p>SERVICE EMAIL: INFO@BROOKMOTIONSERVICE.CA</p>
        </div>
      </address>
    </div>
  </section>
</body>
</html>
```